依頼概要
■依頼の目的/概要
弊社の経営理念を作成しましたが、社内掲示用にポスターの作成をお願いします。

■依頼詳細
ミッション・ビジョン・バリューをポスター1枚に収めてください。
HPにも掲載できればと考えています。

■重視する点
掲載内容は添付ファイルをご確認ください。

過去の提案(同業者なので)を見て応募しようと考えました。
https://www.pitchora.jp/work/detail/4731852

■弊社の紹介
東京都内で廃棄物を収集・処分する会社です。詳しくは下記Official HPをご覧ください。
https://www.miyakura-k.co.jp

HP検討挿入予定個所
https://www.miyakura-k.co.jp/company

■その他
掲載内容の文言はあまり整理されていないのでうまい具合にご調整ください。

■その他ご不明点はお気軽にお問合せください。

発注時のイメージ通りの作品だったため。

この度は、沢山のご応募ありがとうございます。
皆さんのご提案が多く、選定に迷いました。

また機会がございましたら、よろしくお願いします。

```html
<!DOCTYPE html>
<html lang="ja">
<head>
<meta charset="UTF-8">
<title>MIYAKURA 経営理念ポスター</title>
<link rel="stylesheet" href="https://fonts.googleapis.com/css2?family=Montserrat:wght@700&family=Noto+Sans+JP:wght@500;700&family=Noto+Serif:wght@700&display=swap">
<style>
  :root {
    --forest-dark: #1f3a2a;
    --forest-mid: #3f6b4c;
    --sky: #a9c9cf;
    --road: #6f7a7e;
    --road-dark: #4a5356;
    --panel: rgba(22, 86, 98, 0.55);
    --white: #ffffff;
  }
  * { margin: 0; padding: 0; box-sizing: border-box; }
  html, body { width: 846px; height: 1200px; overflow: hidden; background: #ffffff; }
  .poster {
    position: relative;
    width: 846px;
    height: 1200px;
    overflow: hidden;
    font-family: "Noto Sans JP", sans-serif;
    color: var(--white);
  }
  .backdrop {
    position: absolute; inset: 0;
    background:
      radial-gradient(ellipse 30% 22% at 50% 52%, rgba(210,230,232,0.85), rgba(210,230,232,0) 70%),
      linear-gradient(180deg, var(--forest-dark) 0%, var(--forest-mid) 22%, var(--sky) 48%, var(--forest-mid) 62%, var(--road) 80%, var(--road-dark) 100%);
  }
  .panel {
    position: absolute;
    left: 80px; top: 150px;
    width: 686px; height: 940px;
    background: var(--panel);
  }
  .quote {
    position: absolute;
    font-family: "Noto Serif", serif;
    font-weight: 700;
    color: var(--white);
    line-height: 1;
  }
  .quote--close { right: 70px; top: 170px; font-size: 260px; }
  .quote--open { left: 75px; top: 880px; font-size: 260px; }
  .block {
    position: absolute;
    left: 0; width: 846px;
    text-align: center;
  }
  .block__title {
    font-family: "Montserrat", sans-serif;
    font-weight: 700;
    font-size: 58px;
    line-height: 1;
    letter-spacing: 1px;
  }
  .block__subtitle {
    font-weight: 700;
    font-size: 22px;
    margin-top: 10px;
  }
  .block__rule {
    width: 470px; height: 2px;
    margin: 8px auto 0;
    background: var(--white);
  }
  .block__body {
    margin-top: 18px;
    font-weight: 500;
    font-size: 20px;
    line-height: 42px;
  }
  .block--mission { top: 182px; }
  .block--vision { top: 466px; }
  .block--value { top: 792px; }
  .brand {
    position: absolute;
    left: 320px; top: 1110px;
    display: flex; align-items: center; gap: 12px;
  }
  .brand__mark {
    width: 40px; height: 40px; border-radius: 50%;
    background: var(--white);
  }
  .brand__name {
    font-weight: 700;
    font-size: 34px;
    letter-spacing: 1px;
    line-height: 1;
  }
  .brand__sub {
    font-weight: 700;
    font-size: 12px;
    margin-top: 4px;
    letter-spacing: 2px;
  }
</style>
</head>
<body>
<main class="poster">
  <div class="backdrop" role="img" aria-label="森の中をまっすぐ延びる道路と、その先に浮かぶ都市のビル群の風景写真"></div>
  <div class="panel"></div>

  <div class="quote quote--close">”</div>
  <div class="quote quote--open">“</div>

  <section class="block block--mission">
    <h2 class="block__title">Mission</h2>
    <p class="block__subtitle">社会的使命</p>
    <div class="block__rule"></div>
    <p class="block__body">
      地球環境を保全するために、<br>
      静脈産業を支える社会インフラの一部としての役割を全うし、<br>
      すべての人に快適でクリーンな世界を提供する
    </p>
  </section>

  <section class="block block--vision">
    <h2 class="block__title">Vision</h2>
    <p class="block__subtitle">中長計画</p>
    <div class="block__rule"></div>
    <p class="block__body">
      先進的(Advanced)な取り組みを行い<br>
      廃棄物業界リード(Lead)し高品質(High quality)な<br>
      サービスを提供し働きがいのある(Satisfaction)<br>
      会社づくりを行う
    </p>
  </section>

  <section class="block block--value">
    <h2 class="block__title">Value</h2>
    <p class="block__subtitle">大切な価値観</p>
    <div class="block__rule"></div>
    <p class="block__body">
      活発なコミュニケーションの元、情報共有を行い、<br>
      チームワーク溢れる組織風土の中で、<br>
      共働し、何事にも真摯に向き合い、正直な気持ちで、<br>
      チャレンジ行動力をもって、自己実現を目指す
    </p>
  </section>

  <div class="brand">
    <div class="brand__mark"></div>
    <div>
      <div class="brand__name">MIYAKURA</div>
      <div class="brand__sub">宮倉環境サービス株式会社</div>
    </div>
  </div>
</main>
</body>
</html>
```